Internationally renowned Business Coach and Public Speaker needs new Website

I need a website to further support and expand my personal brand - I am a well known entrepreneur, business coach and public speaker on the thema of 'Business Acceleration' and I regularly write articles and have written a popular managementbook on this thema. I would like a new, visually strong and exciting website to explain my background and added value as a business coach and keynote speaker. As a reference I would like to point out the website of Tor Velund (www.torvelund.example).

Target Market(s)

top CEO's of international companies

Industry/Entity Type

Business

Number of Pages Required

1 page

Requirements
Nice to have
• us as a reference: www.torvelund.example

```html
<!DOCTYPE html>
<html lang="en">
<head>
<meta charset="utf-8">
<title>Northvane Business Accelerators</title>
<link href="https://fonts.googleapis.com/css2?family=Oswald:wght@400;500;700&family=Open+Sans:ital,wght@0,400;0,600;1,400&display=swap" rel="stylesheet">
<style>
:root{
  --red:#cc0a0f;
  --red-dark:#a80008;
  --ink:#2b2b2b;
  --muted:#8a8a8a;
  --line:#dedede;
  --dark:#3a3939;
  --darker:#2c2b2b;
  --white:#ffffff;
}
*{margin:0;padding:0;box-sizing:border-box}
html,body{width:704px;height:1200px;overflow:hidden;background:var(--white)}
body{position:relative;font-family:"Open Sans",sans-serif;color:var(--ink);font-size:7px}
.abs{position:absolute}

/* top bar */
.topbar{left:0;top:0;width:704px;height:21px;background:var(--red);color:var(--white);font-size:7.2px}
.topbar .item{position:absolute;top:6px;display:flex;align-items:center;gap:4px}
.topbar .search{position:absolute;left:519px;top:3px;width:127px;height:15px;border:1px solid rgba(255,255,255,.6);font-size:6.4px;padding:3px 5px}
.topbar .search svg{position:absolute;right:4px;top:3px}

/* header */
.brand{left:58px;top:31px;display:flex;align-items:center;gap:6px}
.brand .dot{width:37px;height:37px;border-radius:50%;background:var(--red)}
.brand .name{font-family:"Oswald",sans-serif;font-weight:700;font-size:10px;line-height:9px;color:#666}
.nav{top:47px;left:229px;font-family:"Oswald",sans-serif;font-size:7.4px;color:#333;text-transform:uppercase}
.nav span{position:absolute;white-space:nowrap;color:#333}

/* hero */
.hero{left:58px;top:77px;width:588px;height:255px;overflow:hidden;
  background:
    radial-gradient(ellipse 150px 170px at 62% 38%,#d6d6d6 0%,#b4b4b4 45%,rgba(120,120,120,0) 80%),
    radial-gradient(ellipse 200px 120px at 68% 100%,#151515 0%,#2a2a2a 50%,rgba(40,40,40,0) 85%),
    linear-gradient(90deg,#cfcfcf 0%,#9a9a9a 38%,#5a5a5a 58%,#6e6e6e 80%,#c9c9c9 100%)}
.hero h1{position:absolute;left:39px;top:52px;font-family:"Oswald",sans-serif;font-weight:700;font-size:28px;line-height:30px;color:var(--white);letter-spacing:-.2px}
.hero h1 em{font-style:normal;color:var(--red);display:block}
.hero h2{position:absolute;left:39px;top:113px;font-family:"Oswald",sans-serif;font-weight:700;font-size:15.5px;color:var(--white)}
.hero p{position:absolute;left:40px;top:139px;width:212px;font-family:"Oswald",sans-serif;font-weight:400;font-size:10px;line-height:15px;color:var(--white)}
.btn-red{display:inline-block;background:var(--red);color:var(--white);font-family:"Oswald",sans-serif;text-transform:uppercase}
.hero .btn-red{position:absolute;left:40px;top:178px;width:138px;height:25px;font-size:8px;line-height:25px;text-align:center}
.hero .dots{position:absolute;left:283px;top:241px;display:flex;gap:2px}
.hero .dots i{width:4px;height:4px;border-radius:50%;background:#999}
.hero .dots i:first-child{background:var(--red)}

/* partners */
.partners-title{left:0;width:704px;top:346px;text-align:center;font-family:"Oswald",sans-serif;font-size:11.5px;color:var(--red)}
.partner{top:380px;height:22px;display:flex;align-items:center;gap:4px;font-family:"Oswald",sans-serif;font-weight:500;font-size:13px;color:#4a4a4a}
.partner i{width:12px;height:12px;border-radius:50%;background:#8a8a8a;display:block}

/* service cards */
.card{top:426px;width:185px;height:106px;overflow:hidden}
.card.c1{background:radial-gradient(ellipse 70px 80px at 78% 45%,#7a5a4c 0%,#4a2e28 55%,rgba(40,10,10,0) 100%),linear-gradient(90deg,#141010 0%,#2a0a0a 45%,#6e1410 75%,#3a1a14 100%)}
.card.c2{background:radial-gradient(ellipse 70px 80px at 78% 45%,#8a6a58 0%,#4b3a34 55%,rgba(20,20,40,0) 100%),linear-gradient(90deg,#111 0%,#1a1a22 45%,#283046 75%,#1e2436 100%)}
.card.c3{background:radial-gradient(ellipse 70px 80px at 80% 45%,#8e7060 0%,#5a4640 55%,rgba(60,60,60,0) 100%),linear-gradient(90deg,#1a1a1a 0%,#2a2a2a 45%,#6a6a6a 75%,#8a8a8a 100%)}
.card h3{position:absolute;left:13px;top:14px;font-family:"Oswald",sans-serif;font-weight:400;font-size:13px;color:var(--red)}
.card p{position:absolute;left:14px;top:34px;width:84px;font-size:6.3px;line-height:13.6px;color:var(--white)}
.card .more{position:absolute;left:0;bottom:0;width:185px;height:20px;background:var(--red);color:var(--white);font-family:"Oswald",sans-serif;font-size:7.6px;line-height:20px;padding-left:13px;text-transform:uppercase}
.shadow{top:533px;width:185px;height:6px;background:radial-gradient(ellipse at top,rgba(0,0,0,.18),transparent 70%)}

/* about / speeches */
.sec-title{top:560px;font-family:"Oswald",sans-serif;line-height:1}
.sec-title b{display:block;font-weight:400;font-size:17px;color:var(--red)}
.sec-title span{display:block;margin-top:4px;font-size:10.5px;color:#444;text-transform:uppercase}
.photo{top:608px;width:192px;height:117px}
.photo.studio{background:
    linear-gradient(180deg,rgba(0,0,0,0) 0%,rgba(0,0,0,0) 55%,#0c0f14 56%,#141820 100%),
    linear-gradient(90deg,#1b2c44 0%,#3d8a94 25%,#1a2230 45%,#5aa6a0 60%,#1b2c44 80%,#2a4a6a 100%)}
.photo.stage{background:
    radial-gradient(ellipse 50px 70px at 45% 60%,#2a2a2a 0%,#4a4a4a 50%,rgba(160,160,160,0) 100%),
    linear-gradient(90deg,#f0f0f0 0%,#c8c8c8 45%,#9a9a9a 70%,#d8d8d8 100%)}
.body-text{top:734px;width:196px;font-size:6.3px;line-height:14px;color:var(--muted)}
.sec-btn{top:800px;width:65px;height:20px;font-size:6.3px;line-height:20px;text-align:center}

/* book panel */
.book{left:495px;top:564px;width:151px;height:260px;background:var(--darker)}
.book .cover{height:136px;background:
    linear-gradient(90deg,rgba(0,0,0,0) 0%,rgba(0,0,0,0) 8%,#d8d8d8 8%,#f4f4f4 20%,#c9a870 28%,#f4f4f4 34%,rgba(0,0,0,0) 34%,rgba(0,0,0,0) 56%,#e4e4e4 56%,#c9a870 66%,#f4f4f4 72%,#e8e8e8 92%,rgba(0,0,0,0) 92%) 0 18px/100% 100px no-repeat,
    linear-gradient(180deg,#ffffff 0%,#dedede 100%)}
.book h3{position:absolute;left:16px;top:146px;font-family:"Oswald",sans-serif;font-weight:700;font-size:20px;line-height:22px;letter-spacing:1px}
.book h3 em{font-style:normal;color:var(--red);display:block}
.book h3 span{color:var(--white);display:block}
.book p{position:absolute;left:16px;top:193px;width:126px;font-size:6.3px;line-height:14px;color:#b0b0b0}

/* divider + news */
.divider{left:76px;top:838px;width:380px;height:1px;background:linear-gradient(90deg,transparent,#cfcfcf 20%,#cfcfcf 80%,transparent)}
.arrows-sm{left:456px;top:834px;font-size:7px;color:#aaa}
.news-head{left:57px;top:858px;display:flex;align-items:baseline;gap:6px}
.news-head b{font-family:"Oswald",sans-serif;font-weight:400;font-size:11.5px;color:var(--red)}
.news-head span{font-size:6.8px;color:#666}
.pager{top:860px;display:flex;gap:3px}
.pager i{width:11px;height:11px;border:1px solid #ccc;border-radius:2px;display:block;font-style:normal;font-size:7px;line-height:9px;text-align:center;color:#bbb}
.post{top:888px;width:118px}
.post h4{font-family:"Oswald",sans-serif;font-weight:400;font-size:8.6px;color:#333}
.post .date{margin-top:5px;font-size:6.3px;color:#777}
.post hr{border:0;height:1px;width:26px;background:#ccc;margin:8px 0 9px}
.post p{font-size:6.3px;line-height:13px;color:#777}
.post .read{margin-top:5px;font-size:7px;font-weight:600;color:var(--red);display:flex;align-items:center;gap:3px}

/* testimonial */
.testi{left:495px;top:834px;width:151px;height:152px;background:var(--red);color:var(--white)}
.testi h3{position:absolute;left:0;width:151px;top:16px;text-align:center;font-family:"Oswald",sans-serif;font-weight:400;font-size:17px}
.testi .avatar{position:absolute;left:20px;top:43px;width:42px;height:42px;border-radius:50%;border:2px solid var(--white);background:radial-gradient(circle at 50% 40%,#e2c2ac 0%,#b88e76 45%,#5a3e34 75%,#f2f2f2 76%)}
.testi .who{position:absolute;left:71px;top:55px;font-family:"Oswald",sans-serif;font-size:8.5px}
.testi .who small{display:block;font-family:"Open Sans",sans-serif;font-size:6.2px;margin-top:2px}
.testi blockquote{position:absolute;left:22px;top:94px;width:120px;font-style:italic;font-size:6.4px;line-height:13.6px}
.testi .q{position:absolute;font-family:"Oswald",sans-serif;font-size:12px;opacity:.8}

/* footer */
.footer{left:0;top:1018px;width:704px;height:154px;background:var(--dark);overflow:hidden}
.footer .ghost{position:absolute;left:0;top:4px;font-family:"Oswald",sans-serif;font-weight:700;font-size:66px;line-height:70px;color:rgba(255,255,255,.025);letter-spacing:8px}
.fcol{top:1041px;color:#d5d5d5}
.fcol h5{font-family:"Oswald",sans-serif;font-weight:400;font-size:9.2px;color:var(--white);text-transform:uppercase;margin-bottom:8px}
.fcol p,.fcol li{font-size:6.3px;line-height:13px;color:#bdbdbd;list-style:none}
.email-input{margin-top:6px;width:182px;height:20px;background:var(--white);font-size:6.3px;color:#666;padding:6px 9px}
.sub-btn{margin-top:7px;width:77px;height:19px;font-size:7.4px;line-height:19px;text-align:center}
.contact-row{display:flex;align-items:center;gap:6px}
.socials{display:flex;gap:7px;margin-top:6px}
.socials i{width:16px;height:16px;border-radius:50%;background:#9a9a9a;display:block}
.f-brand{margin-top:10px;font-family:"Oswald",sans-serif;font-weight:700;font-size:13px;line-height:15px;color:#8e8e8e}
.bottombar{left:0;top:1172px;width:704px;height:28px;background:var(--darker);color:#a8a8a8;font-size:6.3px;text-align:center;line-height:28px}
.bottombar span{margin:0 6px}
</style>
</head>
<body>

<div class="abs topbar">
  <div class="item" style="left:59px">
    <svg width="7" height="7" viewBox="0 0 10 10"><path d="M2 1l2 2-1 1.5c.6 1.3 1.4 2 2.5 2.5L7 6l2 2-1.5 1.5C4.5 9 1 5.5.5 2.5z" fill="#fff"/></svg>
    Call Us : ( 5550 ) 410 228
  </div>
  <div class="item" style="left:167px">
    <svg width="8" height="6" viewBox="0 0 10 7"><rect width="10" height="7" fill="#fff"/><path d="M0 0l5 4 5-4" stroke="#cc0a0f" fill="none"/></svg>
    Email Us : info@northvaneaccelerators.example
  </div>
  <div class="search">Search
    <svg width="7" height="7" viewBox="0 0 10 10"><circle cx="4" cy="4" r="3" stroke="#fff" stroke-width="1.5" fill="none"/><path d="M6.3 6.3L9 9" stroke="#fff" stroke-width="1.6"/></svg>
  </div>
</div>

<div class="abs brand">
  <div class="dot"></div>
  <div class="name">Northvane<br>Business<br>Accelerators</div>
</div>
<nav class="abs nav">
  <span style="left:0">Home</span>
  <span style="left:50px">About Us</span>
  <span style="left:112px">Services</span>
  <span style="left:173px">Impact Stories</span>
  <span style="left:254px">Media</span>
  <span style="left:306px">Resources</span>
  <span style="left:374px">Contact Info</span>
</nav>

<section class="abs hero" role="img" aria-label="Black and white portrait of the business coach smiling">
  <h1>Northvane Business<em>Accelerators</em></h1>
  <h2>Business Coach and Public Speaker.</h2>
  <p>I'm a well known entrepreneur, business coach and public speaker.</p>
  <span class="btn-red">Click here for view history &raquo;</span>
  <div class="dots"><i></i><i></i><i></i><i></i></div>
</section>

<div class="abs partners-title">COMPANIES WORKED WITH</div>
<div class="abs partner" style="left:64px"><i></i>Kestrel</div>
<div class="abs partner" style="left:185px;font-size:10px;letter-spacing:2px">LUMENLINE</div>
<div class="abs partner" style="left:276px"><i></i>Swift Folio</div>
<div class="abs partner" style="left:384px">Brightvale</div>
<div class="abs partner" style="left:466px">Heron</div>
<div class="abs partner" style="left:547px"><i></i>Marketon</div>

<article class="abs card c1" style="left:58px" role="img" aria-label="Coach speaking on a red-lit stage, entrepreneur role">
  <h3>ENTREPRENEUR</h3>
  <p>Lorem Ipsum is simply dummy text of the printing and typesetting industry</p>
  <div class="more">View more information &raquo;</div>
</article>
<article class="abs card c2" style="left:260px" role="img" aria-label="Close-up of coach in conversation, business coach role">
  <h3>BUSINESS COACH</h3>
  <p>Lorem Ipsum is simply dummy text of the printing and typesetting industry</p>
  <div class="more">View more information &raquo;</div>
</article>
<article class="abs card c3" style="left:462px" role="img" aria-label="Coach with microphone at a conference, public speaker role">
  <h3>PUBLIC SPEAKER</h3>
  <p>Lorem Ipsum is simply dummy text of the printing and typesetting industry</p>
  <div class="more">View more information &raquo;</div>
</article>
<div class="abs shadow" style="left:58px"></div>
<div class="abs shadow" style="left:260px"></div>
<div class="abs shadow" style="left:462px"></div>

<div class="abs sec-title" style="left:58px"><b>ABOUT</b><span>Northvane Business Accelerators</span></div>
<div class="abs photo studio" style="left:58px" role="img" aria-label="Television studio interview at a round table"></div>
<p class="abs body-text" style="left:58px">Lorem Ipsum is simply dummy text of the printing and typesetting industry. Lorem Ipsum has been the industry's standard dummy text ever since the 1500s, when an unknown printer took a galley of type and scrambled...</p>
<span class="abs btn-red sec-btn" style="left:58px">Read more info</span>

<div class="abs sec-title" style="left:276px"><b>SPEACHES OF</b><span>Northvane Business Accelerators</span></div>
<div class="abs photo stage" style="left:276px" role="img" aria-label="Black and white photo of the coach speaking with a headset"></div>
<p class="abs body-text" style="left:276px">Lorem Ipsum is simply dummy text of the printing and typesetting industry. Lorem Ipsum has been the industry's standard dummy text ever since the 1500s, when an unknown printer took a galley of type and scrambled...</p>
<span class="abs btn-red sec-btn" style="left:276px">Read more info</span>

<aside class="abs book">
  <div class="cover" role="img" aria-label="Front and back of the management book"></div>
  <h3><em>RISING</em><span>DRIVE</span></h3>
  <p>Lorem Ipsum is simply dummy text of the printing and typesetting industry. Lorem Ipsum has been the industry's standard dummy</p>
</aside>

<div class="abs divider"></div>
<div class="abs arrows-sm">&lsaquo; &rsaquo;</div>
<div class="abs news-head"><b>LATEST NEWS</b><span>Lorem Ipsum is simply dummy text of the printing and typesetting industry.</span></div>
<div class="abs pager" style="left:447px"><i>&lsaquo;</i><i>&rsaquo;</i></div>

<article class="abs post" style="left:57px">
  <h4>LOREM IPSUM IS SIMPLY</h4>
  <div class="date">Posted on 27 March 2015</div>
  <hr>
  <p>Lorem Ipsum is simply dummy text of the printing and typesetting industry. has been the industry...</p>
  <div class="read">Read more <svg width="5" height="5" viewBox="0 0 10 10"><circle cx="5" cy="5" r="5" fill="#cc0a0f"/><path d="M4 3l2 2-2 2" stroke="#fff" fill="none" stroke-width="1.4"/></svg></div>
</article>
<article class="abs post" style="left:210px">
  <h4>LOREM IPSUM IS SIMPLY</h4>
  <div class="date">Posted on 27 March 2015</div>
  <hr>
  <p>Lorem Ipsum is simply dummy text of the printing and typesetting industry. has been the industry...</p>
  <div class="read">Read more <svg width="5" height="5" viewBox="0 0 10 10"><circle cx="5" cy="5" r="5" fill="#cc0a0f"/><path d="M4 3l2 2-2 2" stroke="#fff" fill="none" stroke-width="1.4"/></svg></div>
</article>
<article class="abs post" style="left:364px">
  <h4>LOREM IPSUM IS SIMPLY</h4>
  <div class="date">Posted on 27 March 2015</div>
  <hr>
  <p>Lorem Ipsum is simply dummy text of the printing and typesetting industry. has been the industry...</p>
  <div class="read">Read more <svg width="5" height="5" viewBox="0 0 10 10"><circle cx="5" cy="5" r="5" fill="#cc0a0f"/><path d="M4 3l2 2-2 2" stroke="#fff" fill="none" stroke-width="1.4"/></svg></div>
</article>

<aside class="abs testi">
  <h3>TESTIMONIALS</h3>
  <div class="avatar" role="img" aria-label="Portrait of the client giving the testimonial"></div>
  <div class="who">LENA MARSH<small>Business woman</small></div>
  <span class="q" style="left:11px;top:90px">&ldquo;</span>
  <blockquote>Lorem Ipsum is simply dummy text of the printing and typesetting industry. has been the industry...</blockquote>
  <span class="q" style="left:137px;top:122px">&rdquo;</span>
</aside>

<footer class="abs footer">
  <div class="ghost">RISING<br>DRIVE</div>
</footer>

<div class="abs fcol" style="left:59px">
  <h5>Newsletter Signup</h5>
  <p>Get our recent updates through your email id</p>
  <div class="email-input">Enter your email id</div>
  <div class="btn-red sub-btn">Subscribe now</div>
</div>

<div class="abs fcol" style="left:281px">
  <h5>Welcome</h5>
  <ul>
    <li>Home</li><li>About us</li><li>Services</li><li>Impact Stories</li><li>Media</li><li>Resources</li><li>Contact info</li>
  </ul>
</div>

<div class="abs fcol" style="left:376px">
  <h5>Contact Info</h5>
  <p style="color:#fff;font-weight:600">Northvane Business Accelerators</p>
  <p style="margin-top:2px">120 STreet name, City name,<br>Country name : 65236565</p>
  <p class="contact-row" style="margin-top:4px">
    <svg width="7" height="7" viewBox="0 0 10 10"><path d="M2 1l2 2-1 1.5c.6 1.3 1.4 2 2.5 2.5L7 6l2 2-1.5 1.5C4.5 9 1 5.5.5 2.5z" fill="#bdbdbd"/></svg>
    ( 5550 ) 410 228</p>
  <p class="contact-row">
    <svg width="8" height="6" viewBox="0 0 10 7"><rect x=".5" y=".5" width="9" height="6" stroke="#bdbdbd" fill="none"/><path d="M.5 .5l4.5 3.5 4.5-3.5" stroke="#bdbdbd" fill="none"/></svg>
    info@northvaneaccelerators.example</p>
</div>

<div class="abs fcol" style="left:537px">
  <h5>Follow Us</h5>
  <p>Connect with our social network</p>
  <div class="socials"><i></i><i></i><i></i><i></i></div>
  <div class="f-brand">Northvane<br>Business<br>Accelerators</div>
</div>

<div class="abs bottombar">
  &copy; 2015. Northvane Business Accelerators. All rights reserved.<span></span>
  Terms &amp; Conditions<span>/</span>Privacy Policy<span>/</span>Disclaimer
</div>

</body>
</html>
```